Boutique Financial Services/Advisor Business Needs Web Design

Looking for an informational and functional web design for my Financial Services/Financial Advisement business. It should have functionality for Company name, address, phone #, "About Us", Who we are, Our Mission, Services we offer, Biographies/Photos of/about "The Team", and possibly a link to "Contact Us". Would like to see something new & exciting blended with a traditional/professional look that will appeal to those approaching retirement, as well as those younger clients that are beginning to think about planning for the future. I already have a web domain through HostMeadow, but would like this to be the design we use for that domain.
Financial Services/Financial Advisor
Coded - Design and coding required
1 page

```html
<!DOCTYPE html>
<html lang="en">
<head>
<meta charset="utf-8">
<title>Summitline Wealth Management</title>
<link rel="stylesheet" href="https://fonts.googleapis.com/css2?family=Poppins:wght@400;500;600;700;800&display=swap">
<style>
:root{
  --navy:#0b3487;
  --navy-deep:#082a6e;
  --ink:#1d2333;
  --text:#3d4252;
  --muted:#7a7f8c;
  --orange:#f29322;
  --gray-btn:#7d7d7d;
  --light:#f1f2f4;
  --footer:#182340;
  --white:#ffffff;
  --line:#d6d9e0;
}
*{box-sizing:border-box;margin:0;padding:0}
html,body{width:1200px;height:4155px;overflow:hidden}
body{font-family:"Poppins",sans-serif;color:var(--text);background:var(--white);position:relative}
.abs{position:absolute}
.section{position:absolute;left:0;width:1200px}
.btn{position:absolute;display:flex;align-items:center;justify-content:center;font-size:11px;font-weight:500;color:var(--white);border-radius:3px}
.btn-gray{background:var(--gray-btn)}
.btn-orange{background:var(--orange)}
.photo{position:absolute}
.section-title{position:absolute;left:0;width:1200px;display:flex;align-items:center;justify-content:center;gap:12px;font-weight:700;font-size:30px;letter-spacing:.5px}
.section-title .rule{width:26px;height:2px;background:currentColor}
.section-title.on-dark{color:var(--white)}
.section-title.on-dark .rule{background:#6f8ad0}
.section-title.on-light{color:var(--navy)}

/* header */
.site-header{top:0;height:106px;background:var(--white)}
.brand{position:absolute;left:155px;top:34px;display:flex;align-items:center;gap:8px;color:var(--navy);font-weight:600;font-size:15px;letter-spacing:.3px}
.brand-mark{width:14px;height:14px;background:var(--navy)}
.icon-chip{position:absolute;top:22px;width:26px;height:28px;background:#e6e7ea;border-radius:3px;display:flex;align-items:center;justify-content:center}
.main-nav{position:absolute;top:71px;left:440px;display:flex;gap:0;font-size:11px;color:var(--muted)}
.main-nav a{position:absolute;white-space:nowrap;text-decoration:none;color:inherit}
.main-nav a.active{color:var(--orange);text-decoration:underline;text-underline-offset:3px}

/* hero */
.hero{top:106px;height:570px;overflow:hidden}
.hero-title{position:absolute;left:155px;top:142px;font-size:42px;line-height:50px;font-weight:800;color:var(--navy)}

/* about */
.about-title{position:absolute;left:644px;top:722px;font-size:30px;font-weight:700;color:var(--navy);display:flex;align-items:center;gap:8px}
.about-title .rule{width:24px;height:2px;background:var(--navy)}
.about-lead{position:absolute;left:644px;top:772px;width:370px;font-size:12px;line-height:18px;font-weight:700;color:var(--ink)}
.about-body{position:absolute;left:644px;top:842px;width:380px;font-size:10.5px;line-height:17.6px;color:var(--text)}

/* services */
.services{top:1135px;height:660px;background:var(--navy)}
.services-intro{position:absolute;left:160px;top:118px;width:880px;text-align:center;font-size:11px;line-height:15px;color:#dfe6f7}
.service-card{position:absolute;top:191px;width:238px;height:285px}
.service-card .photo{left:0;top:0;width:238px;height:190px;border-radius:4px}
.service-body{position:absolute;left:10px;top:184px;width:220px;height:100px;background:var(--white);border-radius:4px;padding:16px 18px}
.service-body h3{font-size:14px;font-weight:600;color:var(--navy);margin-bottom:6px}
.service-body p{font-size:10.5px;line-height:15px;color:var(--muted)}
.service-card.active h3{color:var(--orange)}
.card-arrow{position:absolute;right:6px;top:-12px;width:26px;height:26px;border-radius:50%;background:var(--orange);display:flex;align-items:center;justify-content:center}

/* mission */
.mission{top:1795px;height:393px;background:var(--light)}
.mission-title{position:absolute;left:156px;top:102px;font-size:29px;line-height:38px;font-weight:700;color:var(--navy)}
.mission-title .rule{display:inline-block;width:26px;height:2px;background:var(--navy);vertical-align:middle;margin-left:4px}
.mission-text{position:absolute;left:156px;top:186px;width:360px;font-size:10.5px;line-height:17.5px;color:var(--ink)}

/* team */
.team{top:2188px;height:497px;background:var(--white)}
.member{position:absolute;top:128px;width:197px;height:230px}
.member .photo{left:0;top:0;width:197px;height:230px}
.member-name{position:absolute;left:0;bottom:12px;width:197px;text-align:center;font-size:12px;font-weight:600;color:var(--white)}
.member-panel{position:absolute;left:843px;top:210px;width:145px}
.member-panel .tag{background:var(--navy);color:var(--white);padding:6px 10px;margin-left:5px}
.member-panel .tag strong{display:block;font-size:11.5px;font-weight:600}
.member-panel .tag span{font-size:9px}
.member-panel p{font-size:9.5px;line-height:14px;color:var(--ink);padding:10px 0 0 15px;width:145px}
.member-panel .connect{display:flex;align-items:center;gap:4px;font-size:10px;font-weight:700;color:var(--ink);padding:8px 0 0 15px}
.member-panel .connect i{width:10px;height:10px;background:var(--navy)}
.member-panel .edge{position:absolute;left:0;top:0;width:3px;height:148px;background:var(--navy)}
.arrow-btn{position:absolute;top:392px;width:31px;height:30px;border-radius:3px;display:flex;align-items:center;justify-content:center}

/* blogs */
.blogs{top:2685px;height:573px;background:var(--navy)}
.blog{position:absolute;top:128px}
.blog .photo{left:0;top:0}
.blog-body{position:absolute;background:var(--white);border-radius:3px;padding:18px 18px}
.blog-date{display:flex;align-items:center;gap:6px;font-size:9.5px;color:var(--navy);margin-bottom:8px}
.blog-body h4{font-size:12px;line-height:19px;font-weight:600;color:var(--ink)}
.date-badge{position:absolute;background:var(--navy);color:var(--white);border:2px solid var(--white);border-radius:4px;text-align:center;padding:6px 4px;width:60px}
.date-badge span{display:block;font-size:10px}
.date-badge strong{display:block;font-size:16px;font-weight:700;line-height:18px}

/* inquiry */
.inquiry{top:3258px;height:330px;background:var(--white)}
.field{position:absolute;border:1px solid var(--line);background:var(--white);font-size:10px;color:#9a9ea8;padding:9px 12px}

/* footer */
.site-footer{top:3580px;height:575px;background:var(--footer)}
.footer-logo{position:absolute;left:156px;top:193px;width:182px;height:127px;background:var(--white);border-radius:3px;display:flex;align-items:center;justify-content:center;gap:6px;color:var(--navy);font-size:13px;font-weight:600}
.footer-logo i{width:12px;height:12px;background:var(--navy)}
.footer-head{position:absolute;top:193px;font-size:13px;font-weight:600;color:var(--orange)}
.contact-line{position:absolute;left:400px;display:flex;gap:8px;font-size:11px;line-height:17px;color:var(--white)}
.quick-links{position:absolute;left:628px;top:222px;list-style:none;font-size:11px;line-height:17.5px;color:var(--white)}
.legal{position:absolute;left:156px;top:360px;width:888px;font-size:9px;line-height:14px;color:#aeb5c6}
.bottom-bar{position:absolute;left:0;top:540px;width:1200px;height:35px;background:var(--orange);color:var(--white);font-size:10px;display:flex;align-items:center;padding:0 156px;justify-content:space-between}
.social{display:flex;gap:10px;align-items:center}
.social .sq{width:12px;height:12px;background:var(--white);border-radius:2px}
.social .ci{width:22px;height:22px;background:var(--ink);border-radius:50%}
</style>
</head>
<body>

<header class="section site-header">
  <div class="brand"><span class="brand-mark"></span>SUMMITLINE WEALTH MANAGEMENT</div>
  <div class="icon-chip" style="left:746px">
    <svg width="12" height="12" viewBox="0 0 24 24"><path d="M6.6 10.8a15 15 0 006.6 6.6l2.2-2.2a1 1 0 011-.25 11.4 11.4 0 003.6.6 1 1 0 011 1V20a1 1 0 01-1 1A17 17 0 013 4a1 1 0 011-1h3.5a1 1 0 011 1c0 1.25.2 2.45.6 3.6a1 1 0 01-.25 1z" fill="#6b7080"/></svg>
  </div>
  <div class="icon-chip" style="left:780px">
    <svg width="12" height="12" viewBox="0 0 24 24"><rect x="2" y="5" width="20" height="14" rx="2" fill="#6b7080"/><path d="M3 6l9 7 9-7" stroke="#e6e7ea" stroke-width="2" fill="none"/></svg>
  </div>
  <div class="btn btn-gray" style="left:820px;top:22px;width:105px;height:30px;gap:6px">
    <svg width="10" height="12" viewBox="0 0 10 12"><rect x="0.5" y="0.5" width="9" height="11" rx="1" fill="none" stroke="#fff"/><rect x="2" y="2" width="6" height="2" fill="#fff"/></svg>Calculators
  </div>
  <div class="btn btn-orange" style="left:933px;top:22px;width:110px;height:30px;gap:6px">
    <svg width="10" height="11" viewBox="0 0 10 11"><circle cx="5" cy="3" r="2.5" fill="none" stroke="#fff"/><path d="M0.5 10.5a4.5 4.5 0 019 0" fill="none" stroke="#fff"/></svg>Client Login
  </div>
  <nav class="main-nav">
    <a class="active" style="left:0">Home</a>
    <a style="left:61px">About Us</a>
    <a style="left:140px">Who we are</a>
    <a style="left:232px">Our Mission</a>
    <a style="left:325px">Services</a>
    <a style="left:401px">The Team</a>
    <a style="left:482px">Blogs</a>
    <a style="left:542px">Contact Us</a>
  </nav>
</header>

<section class="section hero">
  <div class="photo" role="img" aria-label="Hands pointing at a laptop showing financial charts and a world map, with printed reports" style="left:0;top:0;width:1200px;height:570px;background:linear-gradient(100deg,#f4f2ef 0%,#e9e6e2 35%,#c9c6c2 60%,#a8a9ad 80%,#d7c27a 100%)"></div>
  <svg class="abs" style="left:0;top:0" width="1200" height="570" viewBox="0 0 1200 570">
    <polygon points="0,570 0,555 600,450 1200,510 1200,570" fill="#ffffff"/>
    <polygon points="420,500 600,440 760,470 600,460" fill="#0b3487"/>
  </svg>
  <h1 class="hero-title">GROW YOUR<br>BUSINESS MORE<br>EFFICIENCY</h1>
  <div class="btn btn-gray" style="left:155px;top:308px;width:112px;height:30px">Contact Now</div>
</section>

<section class="section" style="top:676px;height:459px">
  <div class="photo" role="img" aria-label="Three advisers reviewing documents together at a desk" style="left:153px;top:19px;width:363px;height:320px;background:linear-gradient(135deg,#3a4a63,#8c8f96 55%,#c9b9a4)"></div>
  <div class="photo" role="img" aria-label="Hand with a magnifier over a printed bar chart" style="left:348px;top:200px;width:222px;height:185px;background:linear-gradient(135deg,#e9ecf1,#8fc4e6 60%,#3e9ad6);border:4px solid #fff"></div>
</section>
<h2 class="about-title">ABOUT US <span class="rule"></span></h2>
<p class="about-lead">Welcome To Our Website, Where You'll Find A Wealth Of Information In The Form Of Newsletter Articles, Calculators, And Research Reports.</p>
<p class="about-body">We Hope Your Visit Will Help You Understand The Opportunities And Potential Rewards That Are Available When You Take A Proactive Approach To Your Personal Financial Situation. We Have Created This Web Site To Help You Gain A Better Understanding Of The Financial Concepts Behind Insurance, Investing, Retirement, Estate Planning, And Wealth Preservation. Most Important, We Hope You See The Value Of Working With Skilled Professionals To Pursue Your Financial Goals.</p>
<div class="btn btn-gray" style="left:644px;top:992px;width:96px;height:30px">Read More</div>

<section class="section services">
  <h2 class="section-title on-dark" style="top:66px"><span class="rule"></span>SERVICES<span class="rule"></span></h2>
  <p class="services-intro">While developing a customized financial program, we will walk you through a step-by-step process that will help make you feel confident in your decisions. Once your goals have been established, we will customize appropriate strategies to suit your vision and objectives. We can help you execute a sound financial program utilizing the following products and services:</p>

  <article class="service-card" style="left:12px">
    <div class="photo" role="img" aria-label="Couple reviewing estate documents" style="background:linear-gradient(135deg,#5c5a5a,#b9b3ad)"></div>
    <div class="service-body"><h3>Estate Planning</h3><p>Lorem Ipsum is simply dummy text of the printing &amp; typesetting industry.</p></div>
  </article>
  <article class="service-card" style="left:262px">
    <div class="photo" role="img" aria-label="Retired couple reading paperwork outdoors" style="background:linear-gradient(135deg,#c9d2a6,#8f8570 60%,#d8cfb5)"></div>
    <div class="service-body"><h3>Retirement Planning</h3><p>Lorem Ipsum is simply dummy text of the printing &amp; typesetting industry.</p></div>
  </article>
  <article class="service-card active" style="left:512px">
    <div class="photo" role="img" aria-label="Banknotes handed over a desk" style="background:linear-gradient(135deg,#d9dbde,#9ea2a7 60%,#5f6a57)"></div>
    <div class="service-body">
      <span class="card-arrow"><svg width="12" height="12" viewBox="0 0 12 12"><path d="M2 6h8M7 3l3 3-3 3" stroke="#fff" stroke-width="1.5" fill="none"/></svg></span>
      <h3>Financial Planning</h3><p>Lorem Ipsum is simply dummy text of the printing &amp; typesetting industry.</p>
    </div>
  </article>
  <article class="service-card" style="left:762px">
    <div class="photo" role="img" aria-label="Large gold tax letters on coins" style="background:linear-gradient(135deg,#e9e7e2,#d8b55a 55%,#8d7a4c)"></div>
    <div class="service-body"><h3>Tax Planning</h3><p>Lorem Ipsum is simply dummy text of the printing &amp; typesetting industry.</p></div>
  </article>
  <article class="service-card" style="left:1012px">
    <div class="photo" role="img" aria-label="Coin dropped into a jar beside growing plants" style="background:linear-gradient(135deg,#3e4040,#8b8d84 60%,#6f8a4f)"></div>
    <div class="service-body"><h3>Wealth Management</h3><p>Lorem Ipsum is simply dummy text of the printing &amp; typesetting industry.</p></div>
  </article>

  <div class="abs" style="left:616px;top:508px;width:16px;height:16px;border-radius:4px;background:#3b5fb0;border:2px solid #8aa3dd"></div>
  <div class="btn btn-orange" style="left:584px;top:555px;width:81px;height:29px">View All</div>
</section>

<section class="section mission">
  <h2 class="mission-title">OUR MISSION<br>STATEMENT<span class="rule"></span></h2>
  <div class="mission-text">
    <p>We Are Committed To Maintaining The Highest Standards Of Integrity And Professionalism In Our Relationship With You, Our Client.</p>
    <p style="margin-top:17px">We Endeavor To Know And Understand Your Financial Situation And Provide You With Only The Highest Quality Information, Services, And Products To Help You Reach Your Goals.</p>
  </div>
  <div class="photo" role="img" aria-label="Hand touching a digital screen with the word mission and hexagon icons" style="left:587px;top:75px;width:456px;height:243px;background:linear-gradient(120deg,#1c1c1e,#5a5b5e 55%,#2a2a2c)"></div>
</section>

<section class="section team">
  <h2 class="section-title on-light" style="top:68px"><span class="rule"></span>OUR TEAM<span class="rule"></span></h2>
  <div class="member" style="left:203px">
    <div class="photo" role="img" aria-label="Portrait of team member Kara Lindell" style="background:linear-gradient(180deg,#d9d9d9,#4a4a4a)"></div>
    <div class="member-name">Kara Lindell</div>
  </div>
  <div class="member" style="left:425px">
    <div class="photo" role="img" aria-label="Portrait of team member Miles Carver" style="background:linear-gradient(180deg,#cfcfcf,#3d3d3d)"></div>
    <div class="member-name">Miles Carver</div>
  </div>
  <div class="member" style="left:646px">
    <div class="photo" role="img" aria-label="Colour portrait of team member Nora Y. Reed" style="background:linear-gradient(180deg,#f1f1f1,#c9a98c 60%,#e3e3e3)"></div>
  </div>
  <div class="member-panel">
    <span class="edge"></span>
    <div class="tag"><strong>Nora Y. Reed</strong><span>President &amp; CEO</span></div>
    <p>Lorem Ipsum Is Simply Dummy Text Of The Printing And Typesetting Industry. Lorem Ipsum Has Been The Industry's Standard...</p>
    <div class="connect">Connect<i></i></div>
  </div>
  <div class="btn btn-gray" style="left:521px;top:392px;width:80px;height:30px">View All</div>
  <div class="arrow-btn" style="left:613px;background:#7d7d7d"><svg width="10" height="10" viewBox="0 0 10 10"><path d="M6.5 1.5L3 5l3.5 3.5" stroke="#fff" stroke-width="1.5" fill="none"/></svg></div>
  <div class="arrow-btn" style="left:647px;background:var(--orange)"><svg width="10" height="10" viewBox="0 0 10 10"><path d="M3.5 1.5L7 5 3.5 8.5" stroke="#fff" stroke-width="1.5" fill="none"/></svg></div>
</section>

<section class="section blogs">
  <h2 class="section-title on-dark" style="top:64px"><span class="rule"></span>OUR BLOGS<span class="rule"></span></h2>

  <article class="blog" style="left:156px">
    <div class="photo" role="img" aria-label="Hands with a pen over printed financial charts" style="width:374px;height:200px;background:linear-gradient(135deg,#eef1f4,#a9b8c8 60%,#e6b684)"></div>
    <div class="blog-body" style="left:16px;top:200px;width:340px;height:105px;padding-top:44px"><h4>Lorem Ipsum Is Simply Dummy Text Of The Printing And Typesetting Industry...</h4></div>
    <div class="date-badge" style="left:36px;top:175px"><span>Nov 26</span><strong>2024</strong></div>
  </article>

  <article class="blog" style="left:556px">
    <div class="photo" role="img" aria-label="Tablet showing a blue bar chart beside paperwork" style="width:231px;height:200px;background:linear-gradient(135deg,#dfe7ef,#8fb4d8 60%,#eef2f6)"></div>
    <div class="blog-body" style="left:7px;top:200px;width:217px;height:105px">
      <div class="blog-date"><svg width="10" height="10" viewBox="0 0 10 10"><rect x="0.5" y="1.5" width="9" height="8" fill="none" stroke="#0b3487"/><path d="M0.5 4h9" stroke="#0b3487"/></svg>Nov 26, 2024</div>
      <h4>Lorem Ipsum Is Simply Dummy Text Of The Printing &amp;Typesetting Industry...</h4>
    </div>
  </article>

  <article class="blog" style="left:813px">
    <div class="photo" role="img" aria-label="Adviser writing notes at a bright desk" style="width:230px;height:200px;background:linear-gradient(135deg,#f3f3f3,#b7bcc3 60%,#e9e9e9)"></div>
    <div class="blog-body" style="left:7px;top:200px;width:216px;height:105px">
      <div class="blog-date"><svg width="10" height="10" viewBox="0 0 10 10"><rect x="0.5" y="1.5" width="9" height="8" fill="none" stroke="#0b3487"/><path d="M0.5 4h9" stroke="#0b3487"/></svg>Nov 26, 2024</div>
      <h4>Lorem Ipsum Is Simply Dummy Text Of The Printing &amp;Typesetting Industry...</h4>
    </div>
  </article>

  <div class="btn btn-orange" style="left:560px;top:468px;width:80px;height:30px">View All</div>
</section>

<section class="section inquiry">
  <h2 class="section-title on-light" style="top:68px"><span class="rule"></span>QUICK INQUIRY<span class="rule"></span></h2>
  <div class="field" style="left:325px;top:127px;width:268px;height:33px">First Name</div>
  <div class="field" style="left:606px;top:127px;width:269px;height:33px">Last Name</div>
  <div class="field" style="left:325px;top:177px;width:268px;height:33px">Email</div>
  <div class="field" style="left:606px;top:177px;width:269px;height:33px">Phone</div>
  <div class="field" style="left:325px;top:225px;width:550px;height:85px">How Can We Help?</div>
</section>

<footer class="section site-footer">
  <svg class="abs" style="left:0;top:0" width="1200" height="180" viewBox="0 0 1200 180">
    <polygon points="0,0 1200,0 1200,8 600,100 0,8" fill="#ffffff"/>
    <polygon points="0,8 600,100 1200,8 1200,70 600,140 0,70" fill="#1f2c4f"/>
    <polygon points="330,110 600,140 870,110 600,160" fill="#0b3487"/>
  </svg>
  <div class="btn btn-gray" style="left:560px;top:10px;width:80px;height:30px">Submit</div>

  <div class="footer-logo"><i></i>SUMMITLINE WEALTH</div>

  <div class="footer-head" style="left:400px">CONTACT US</div>
  <div class="contact-line" style="top:222px"><svg width="10" height="12" viewBox="0 0 24 24"><path d="M6.6 10.8a15 15 0 006.6 6.6l2.2-2.2a1 1 0 011-.25 11.4 11.4 0 003.6.6 1 1 0 011 1V20a1 1 0 01-1 1A17 17 0 013 4a1 1 0 011-1h3.5a1 1 0 011 1c0 1.25.2 2.45.6 3.6a1 1 0 01-.25 1z" fill="#f29322"/></svg>555-014-2290</div>
  <div class="contact-line" style="top:247px"><svg width="10" height="12" viewBox="0 0 24 24"><rect x="2" y="5" width="20" height="14" rx="2" fill="#f29322"/></svg>info@summitlinewealth.com</div>
  <div class="contact-line" style="top:272px"><svg width="10" height="12" viewBox="0 0 24 24"><path d="M12 2a7 7 0 00-7 7c0 5 7 13 7 13s7-8 7-13a7 7 0 00-7-7zm0 9.5A2.5 2.5 0 1112 6.5a2.5 2.5 0 010 5z" fill="#f29322"/></svg><span>1420 Harlow Avenue, Suite 210<br>Fairview, OH</span></div>

  <div class="footer-head" style="left:628px">QUICK LINKS</div>
  <ul class="quick-links">
    <li>Home</li><li>About Us</li><li>Who we are</li><li>Our Mission</li><li>Services</li><li>The Team</li><li>Blogs</li><li>Contact Us</li>
  </ul>

  <div class="photo" role="img" aria-label="Street map showing the office location" style="left:793px;top:193px;width:250px;height:150px;background:linear-gradient(135deg,#e8eaed,#d4dbe6 50%,#eef0f2);border-radius:3px"></div>

  <p class="legal">Securities and Advisory Services are offered through Keystone Planners Financial Services, member of the national broker registry. Summitline Wealth Management and Keystone Planners are independent companies. Our representative is registered to conduct securities business in select states only. This communication is strictly intended for individuals residing in the states listed. No offers may be made or accepted from outside the specific states referenced. Insurance-related services may not be provided to individuals residing in any states other than those listed. A broker-dealer, investment adviser, agent, or representative may only transact business in a state if first registered appropriately. Follow-up or individualized responses to persons in a state by such a firm or individual that involve effecting or attempting to effect transactions in securities, or the rendering of personalized investment advice for compensation, will not be made without first complying with appropriate registration requirements. Links are provided for informational purposes only and should not be viewed as an endorsement, sponsorship, solicitation or other affiliation with respect to any third parties or their content. Keystone Planners has not reviewed the content of, and is not responsible for, the information or the results of the third-party.</p>

  <div class="bottom-bar">
    <span>Copyright © 2024 Summitline. All rights reserved</span>
    <span class="social"><span class="sq"></span><span class="sq"></span><span class="ci"></span></span>
  </div>
</footer>

</body>
</html>
```